Need a professional appearance with as much information about the company as possible without being to much (if that makes sense). We are a ambulance company. Would like our list of services on the back (which i can email later, theres about ) along with our legal business name (Harlow TransCare LLC). Ive attached our logo that was designed for us 6 years ago. would like for the star of life to be have the metallic appearance. These are just my ideas, I'm not a professional designer so am open to all ideas.

```html
<!DOCTYPE html>
<html lang="en">
<head>
<meta charset="utf-8">
<title>Harlow TransCare – Business Card</title>
<link rel="stylesheet" href="https://fonts.googleapis.com/css2?family=Source+Sans+3:wght@400;600&family=Fondamento&display=swap">
<style>
  :root {
    --page: #ffffff;
    --stage: #cfcfcf;
    --card-dark: #1f1d1e;
    --card-mid: #2e2c2d;
    --card-side: #3a393b;
    --teal: #2aaabb;
    --teal-bar: #23a3b4;
    --ink-light: #ffffff;
    --card-edge: #f2f2f2;
  }
  * { box-sizing: border-box; margin: 0; padding: 0; }
  html, body {
    width: 1200px; height: 982px; overflow: hidden;
    background: var(--page);
    font-family: "Source Sans 3", "Myriad Pro", sans-serif;
    color: var(--ink-light);
  }
  .stage {
    position: absolute; left: 22px; top: 38px;
    width: 1111px; height: 834px;
    background: var(--stage);
  }
  .card {
    position: absolute; width: 667px; height: 381px;
    border: 1px solid var(--card-edge);
    overflow: hidden;
    background: linear-gradient(90deg, var(--card-mid) 0%, var(--card-dark) 100%);
    box-shadow: 0 2px 6px rgba(0,0,0,.25);
  }
  .card--front { left: 74px; top: 74px; }
  .card--back { left: 430px; top: 472px; }
  .card__band { position: absolute; inset: 0; width: 100%; height: 100%; }

  .brand {
    position: absolute; left: 0; right: 0; top: 58px;
    display: flex; align-items: center; justify-content: center; gap: 14px;
    padding-left: 150px;
  }
  .brand__dot { width: 22px; height: 22px; border-radius: 50%; background: var(--teal); }
  .brand__name { font-size: 44px; font-weight: 600; letter-spacing: .5px; }

  .contact-bar {
    position: absolute; right: 0; height: 31px;
    background: var(--teal-bar);
    box-shadow: 0 2px 3px rgba(0,0,0,.45);
    display: flex; align-items: center;
    font-size: 19px;
  }
  .contact-bar svg { width: 22px; height: 22px; margin-right: 12px; flex: none; }
  .contact-bar--1 { left: 218px; top: 192px; padding-left: 20px; }
  .contact-bar--2 { left: 236px; top: 229px; padding-left: 28px; }
  .contact-bar--3 { left: 256px; top: 265px; padding-left: 30px; }
  .contact-bar--3 svg { margin-right: 26px; }
  .contact-bar--4 { left: 276px; top: 301px; padding-left: 30px; }
  .contact-bar--5 { left: 296px; top: 337px; padding-left: 30px; }
  .contact-bar--5 svg { margin-right: 20px; }

  .services__title {
    position: absolute; left: 156px; top: 24px;
    font-family: "Fondamento", serif; font-size: 24px;
  }
  .services__item { position: absolute; font-size: 15px; white-space: nowrap; }
</style>
</head>
<body>
<div class="stage"></div>

<section class="card card--front">
  <svg class="card__band" viewBox="0 0 667 381" aria-hidden="true">
    <defs>
      <filter id="band-shadow" x="-20%" y="-20%" width="140%" height="140%">
        <feDropShadow dx="6" dy="0" stdDeviation="6" flood-color="#000" flood-opacity=".55"/>
      </filter>
    </defs>
    <polygon points="0,100 156,381 0,381" fill="var(--card-side)"/>
    <polygon points="0,0 108,0 322,381 156,381 0,100" fill="var(--teal)" filter="url(#band-shadow)"/>
  </svg>

  <div class="brand">
    <span class="brand__dot"></span>
    <span class="brand__name">Harlow TransCare</span>
  </div>

  <div class="contact-bar contact-bar--1">
    <svg viewBox="0 0 24 24" aria-hidden="true"><path d="M12 3 2 12h3v9h5v-6h4v6h5v-9h3z" fill="#fff"/></svg>
    418 Linden Avenue Millbrook, GA 30612
  </div>
  <div class="contact-bar contact-bar--2">
    <svg viewBox="0 0 24 24" aria-hidden="true"><rect x="2" y="5" width="20" height="14" fill="none" stroke="#fff" stroke-width="1.6"/><path d="M2 5l10 8 10-8M2 19l7-7M22 19l-7-7" fill="none" stroke="#fff" stroke-width="1.6"/></svg>
    P.O. Box 7415 Millbrook, GA 30614
  </div>
  <div class="contact-bar contact-bar--3">
    <svg viewBox="0 0 24 24" aria-hidden="true"><path d="M6.6 2.5 9.5 7 7.8 9a12 12 0 0 0 7.2 7.2l2-1.7 4.5 2.9-1.6 3.6C12 21 3 12 2.9 4.1z" fill="#fff"/></svg>
    555.014.2278
  </div>
  <div class="contact-bar contact-bar--4">
    <svg viewBox="0 0 24 24" aria-hidden="true"><path d="M2 10l10-7 10 7v11H2z" fill="#fff"/><rect x="6" y="8" width="12" height="7" fill="var(--teal-bar)"/><path d="M2 10l10 7 10-7" fill="none" stroke="var(--teal-bar)" stroke-width="1.4"/></svg>
    info@harlowtranscare.com
  </div>
  <div class="contact-bar contact-bar--5">
    <svg viewBox="0 0 24 24" aria-hidden="true"><circle cx="12" cy="12" r="10" fill="#fff"/><circle cx="8" cy="13" r="1.3" fill="var(--card-dark)"/><circle cx="12" cy="13" r="1.3" fill="var(--card-dark)"/><circle cx="16" cy="13" r="1.3" fill="var(--card-dark)"/></svg>
    www.HarlowTransCare.com
  </div>
</section>

<section class="card card--back">
  <svg class="card__band" viewBox="0 0 667 381" aria-hidden="true">
    <defs>
      <filter id="band-shadow-back" x="-20%" y="-20%" width="140%" height="140%">
        <feDropShadow dx="6" dy="0" stdDeviation="6" flood-color="#000" flood-opacity=".55"/>
      </filter>
    </defs>
    <polygon points="0,100 165,381 0,381" fill="var(--card-side)"/>
    <polygon points="0,0 110,0 325,381 165,381 0,100" fill="var(--teal)" filter="url(#band-shadow-back)"/>
  </svg>

  <h2 class="services__title">Services Provided:</h2>

  <span class="services__item" style="left:175px;top:78px">Hospital &amp; Nursing Home Discharges</span>
  <span class="services__item" style="left:199px;top:114px">Doctors Appointments</span>
  <span class="services__item" style="left:218px;top:150px">Hospital Transfers</span>
  <span class="services__item" style="left:239px;top:186px">Surgical Procedures</span>
  <span class="services__item" style="left:263px;top:222px">Chemotherapy</span>
  <span class="services__item" style="left:282px;top:258px">Dire Admits</span>
  <span class="services__item" style="left:301px;top:295px">Long Distance</span>
  <span class="services__item" style="left:325px;top:331px">Hospice</span>

  <span class="services__item" style="left:470px;top:79px">Dialysis</span>
  <span class="services__item" style="left:480px;top:115px">Imaging Services</span>
  <span class="services__item" style="left:495px;top:151px">Wheel Chair</span>
  <span class="services__item" style="left:511px;top:187px">Wound Care</span>
  <span class="services__item" style="left:524px;top:223px">Infusion</span>
  <span class="services__item" style="left:534px;top:259px">ER Transfers</span>
  <span class="services__item" style="left:552px;top:296px">Bariatric</span>
  <span class="services__item" style="left:569px;top:332px">Radiation</span>
</section>
</body>
</html>
```